wooden jewelry - pearl necklaces

I sell wooden jeweler (rings and pearls) on markets, and so on. I also opened my business as a carpenter. The rings and a combination of wood and metal. The wood is special wood, not very common on Europe. I paint the rings afterwards. You can see some of the pictures on the pictures I uploaded. The pearls are made of the same kind of wood and colored in all kinds of colors. They are then assembled to bracelets. The jewelry is very individual and looks really cool and all kinds of people.

Target Market(s)

Young urban alternative with a sense of individuality

Contact Information for Business Card

Front:

Text:

„Kugelwerk“ (big)
„Malte Oswitz“ (smaler)

Back
„Holzschmuck
Herstellung von individuellem Holz- und Modeschmuck

Malte Oswitz
Tel: 015239460518
Lindgarbweg 9
83127 Auenthal

malteoswitz@postfeld.de“

Font styles to use
Sans Serif

Requirements
Nice to have
• Nice to see a camel thorn tree on the background, this is a special wood and some of the rings are made out of this wood.

```html
<!DOCTYPE html>
<html lang="de">
<head>
<meta charset="utf-8">
<title>Kugelwerk – Visitenkarte</title>
<link rel="stylesheet" href="https://fonts.googleapis.com/css2?family=Cinzel:wght@400;700&family=Alex+Brush&display=swap">
<style>
  :root {
    --stage: #e9e6e1;
    --ink-white: #ffffff;
    --panel-black: #1a1a1a;
    --panel-edge: #8a8a8a;
    --bead-dark: #3b2230;
    --bead-warm: #b07a3c;
    --bead-light: #e8d3a4;
    --bead-red: #a8283f;
    --wood-deep: #7a2a10;
    --wood-mid: #b4461a;
    --wood-light: #cf6a2c;
    --ring-steel: #9aa3ad;
    --ring-wood: #6e3422;
  }
  * { box-sizing: border-box; margin: 0; padding: 0; }
  html, body { width: 1200px; height: 900px; overflow: hidden; background: var(--stage); }
  .canvas { position: relative; width: 1200px; height: 900px; }

  .card {
    position: absolute; left: 280px; width: 640px; height: 400px;
    border-radius: 22px; overflow: hidden;
    box-shadow: 0 6px 18px rgba(0,0,0,.18);
  }
  .card--front { top: 40px; }
  .card--back { top: 460px; }

  /* Front */
  .bead-photo {
    position: absolute; inset: 0;
    background:
      radial-gradient(circle at 20% 30%, var(--bead-light) 0 12%, transparent 30%),
      radial-gradient(circle at 75% 70%, var(--bead-warm) 0 10%, transparent 32%),
      radial-gradient(circle at 85% 20%, var(--bead-red) 0 6%, transparent 22%),
      radial-gradient(circle at 30% 80%, var(--bead-dark) 0 10%, transparent 30%),
      linear-gradient(135deg, var(--bead-warm), var(--bead-dark) 50%, var(--bead-light));
  }
  .name-panel {
    position: absolute; left: 100px; top: 120px; width: 440px; height: 160px;
    background: var(--panel-black); border: 2px solid var(--panel-edge);
    display: flex; flex-direction: column; align-items: center; justify-content: center;
    color: var(--ink-white); font-family: "Cinzel", serif; text-align: center;
  }
  .brand-name { font-size: 56px; font-weight: 700; letter-spacing: 1px; line-height: 1; }
  .owner-name { font-size: 30px; font-weight: 700; margin-top: 10px; letter-spacing: 1px; }

  /* Back */
  .card--back {
    background: linear-gradient(100deg, var(--wood-deep), var(--wood-mid) 35%, var(--wood-light) 60%, var(--wood-mid) 85%, var(--wood-deep));
    color: var(--ink-white); font-family: "Cinzel", serif;
  }
  .tagline { position: absolute; top: 34px; left: 0; right: 0; text-align: center; line-height: 1.3; }
  .tagline__title { font-size: 28px; font-weight: 700; letter-spacing: 2px; }
  .tagline__line { font-size: 24px; font-weight: 700; letter-spacing: 2px; }
  .rings-photo {
    position: absolute; left: 30px; top: 200px; width: 250px; height: 170px; border-radius: 50%;
    background: radial-gradient(ellipse at 45% 45%, var(--ring-steel), var(--ring-wood) 65%, rgba(110,52,34,0) 100%);
  }
  .signature {
    position: absolute; right: 60px; top: 196px;
    font-family: "Alex Brush", cursive; font-size: 54px; line-height: 1;
  }
  .contact { position: absolute; right: 24px; top: 278px; list-style: none; text-align: right; font-size: 17px; font-weight: 700; letter-spacing: 1px; line-height: 1.45; }
  .contact li { display: flex; justify-content: flex-end; align-items: center; gap: 10px; }
  .contact svg { width: 16px; height: 16px; flex: none; }
  .contact .no-icon { padding-right: 26px; }
</style>
</head>
<body>
<main class="canvas">
  <section class="card card--front">
    <div class="bead-photo" role="img" aria-label="Foto bunter Holzperlen in Rot, Beige, Braun und Violett"></div>
    <div class="name-panel">
      <div class="brand-name">Kugelwerk</div>
      <div class="owner-name">Malte Oswitz</div>
    </div>
  </section>

  <section class="card card--back">
    <div class="tagline">
      <div class="tagline__title">Holzschmuck</div>
      <div class="tagline__line">Herstellung von individuellem</div>
      <div class="tagline__line">Holz- und Modeschmuck</div>
    </div>
    <div class="rings-photo" role="img" aria-label="Foto dreier Ringe aus Holz und Edelstahl"></div>
    <div class="signature">Malte Oswitz</div>
    <ul class="contact">
      <li>015239460518
        <svg viewBox="0 0 16 16" aria-hidden="true"><rect x="4" y="1" width="8" height="14" rx="1.5" fill="none" stroke="#fff" stroke-width="1.5"/><line x1="7" y1="12.5" x2="9" y2="12.5" stroke="#fff" stroke-width="1.5"/></svg></li>
      <li>malteoswitz@postfeld.de
        <svg viewBox="0 0 16 16" aria-hidden="true"><rect x="1" y="3" width="14" height="10" fill="#fff"/><path d="M1 3l7 6 7-6" fill="none" stroke="#b4461a" stroke-width="1.3"/></svg></li>
      <li>Lindgarbweg 9
        <svg viewBox="0 0 16 16" aria-hidden="true"><path d="M8 15s-5-5.5-5-9a5 5 0 0 1 10 0c0 3.5-5 9-5 9z" fill="#fff"/><circle cx="8" cy="6" r="1.8" fill="#b4461a"/></svg></li>
      <li class="no-icon">83127 Auenthal</li>
    </ul>
  </section>
</main>
</body>
</html>
```